Letterhead

We would like to use the logo attached as a new letterhead. Our problem is that we think the dark blue background is too much. We'd like a sleek, professional letterhead, and we'd like at least five options to choose from. I've also uploaded our old letterhead for reference of the style we're going for.

```html
<!DOCTYPE html>
<html lang="en">
<head>
<meta charset="utf-8">
<title>Stationery Set – Quorum Hall Strategies</title>
<link rel="stylesheet" href="https://fonts.googleapis.com/css2?family=Cinzel:wght@500&family=Cormorant+Garamond:wght@500;600&family=Open+Sans:wght@700&display=swap">
<style>
  :root {
    --board-grey: #dcdddf;
    --board-tan: #c8b790;
    --navy: #1b2f4e;
    --gold: #c9a765;
    --label-grey: #5a5b5e;
    --paper: #ffffff;
  }
  * { margin: 0; padding: 0; box-sizing: border-box; }
  html, body { width: 1200px; height: 933px; overflow: hidden; }
  body {
    position: relative;
    background: var(--board-grey);
    font-family: "Cormorant Garamond", Georgia, serif;
  }
  .board-accent { position: absolute; inset: 0; width: 1200px; height: 933px; }

  .piece-label {
    position: absolute;
    font-family: "Open Sans", Arial, sans-serif;
    font-weight: 700;
    font-size: 21px;
    color: var(--label-grey);
    letter-spacing: -0.2px;
  }
  .label-letterhead { left: 55px; top: 141px; }
  .label-env-front { left: 597px; top: 151px; }
  .label-env-back { left: 597px; top: 472px; }

  .sheet {
    position: absolute;
    background: var(--paper);
    box-shadow: 0 6px 18px rgba(0,0,0,0.35);
    overflow: hidden;
  }

  .brand-name {
    font-family: "Cinzel", "Times New Roman", serif;
    font-weight: 500;
    color: var(--navy);
    letter-spacing: 1.5px;
    white-space: nowrap;
  }

  /* Letterhead */
  .letterhead { left: 55px; top: 183px; width: 474px; height: 613px; }
  .letterhead .brand-name {
    position: absolute; top: 24px; left: 0; right: 0;
    text-align: center; font-size: 20px;
  }
  .signatory {
    position: absolute; top: 531px; left: 0; right: 0;
    text-align: center; color: var(--navy);
  }
  .signatory-name { font-size: 16px; font-weight: 600; letter-spacing: 1px; }
  .signatory-role { font-size: 11.5px; font-weight: 500; letter-spacing: 0.6px; margin-top: 1px; }

  .gold-rule { position: absolute; left: 0; right: 0; height: 1px; background: var(--gold); }
  .navy-band {
    position: absolute; left: 0; right: 0; bottom: 0;
    background: var(--navy);
    display: flex; align-items: center;
    color: var(--gold);
    font-size: 11px; font-weight: 500;
    white-space: nowrap;
  }
  .letterhead .gold-rule { top: 573px; }
  .letterhead .navy-band { height: 35px; padding-left: 17px; }

  .contact-item { display: inline-flex; align-items: center; gap: 3px; }
  .contact-sep { margin: 0 4px; }
  .icon { width: 8px; height: 9px; fill: var(--gold); flex: none; }

  /* Envelope front */
  .envelope-front { left: 597px; top: 196px; width: 528px; height: 230px; }
  .envelope-front .brand-name {
    position: absolute; left: 16px; top: 148px; font-size: 20px;
  }
  .envelope-front .gold-rule { top: 190px; }
  .envelope-front .navy-band { height: 36px; padding-left: 17px; }

  /* Envelope back */
  .envelope-back { left: 597px; top: 515px; width: 528px; height: 230px; }
  .envelope-flap { position: absolute; left: 0; top: 0; width: 528px; height: 90px; }
</style>
</head>
<body>
  <svg class="board-accent" viewBox="0 0 1200 933" aria-hidden="true">
    <polygon points="1200,0 1200,933 469,933" fill="var(--board-tan)"/>
  </svg>

  <h2 class="piece-label label-letterhead">Letterhead Design_2</h2>
  <h2 class="piece-label label-env-front">Envelope Front Design_2</h2>
  <h2 class="piece-label label-env-back">Envelope Back Design_2</h2>

  <section class="sheet letterhead">
    <div class="brand-name">Quorum Hall Strategies</div>
    <div class="signatory">
      <div class="signatory-name">Harold J. Wrenfield, PC</div>
      <div class="signatory-role">Governmental Affairs Consulting, Attorney at Law</div>
    </div>
    <div class="gold-rule"></div>
    <footer class="navy-band">
      <span class="contact-item">
        <svg class="icon" viewBox="0 0 8 10"><path d="M4 0a3.5 3.5 0 0 0-3.5 3.5C.5 6 4 10 4 10s3.5-4 3.5-6.5A3.5 3.5 0 0 0 4 0zm0 5a1.4 1.4 0 1 1 0-2.8A1.4 1.4 0 0 1 4 5z"/></svg>
        218 K Avenue, Suite 310, Juneau, Alaska 99802</span><span class="contact-sep">|</span>
      <span class="contact-item">
        <svg class="icon" viewBox="0 0 10 10"><path d="M2.2 0.5l1.6 2-1 1.1c.6 1.3 1.5 2.2 2.6 2.7l1.1-1 2 1.6-1 2.1C3.8 8.8 1.2 6.2.2 1.5z"/></svg>
        555 014 2287</span><span class="contact-sep">|</span>
      <span class="contact-item">
        <svg class="icon" viewBox="0 0 10 8"><path d="M0 0h10v8H0zM1 1l4 3 4-3v-.2H1z" fill-rule="evenodd"/></svg>
        harold@wrenfieldlaw.com</span>
    </footer>
  </section>

  <section class="sheet envelope-front">
    <div class="brand-name">Quorum Hall Strategies</div>
    <div class="gold-rule"></div>
    <footer class="navy-band">
      <span class="contact-item">
        <svg class="icon" viewBox="0 0 8 10"><path d="M4 0a3.5 3.5 0 0 0-3.5 3.5C.5 6 4 10 4 10s3.5-4 3.5-6.5A3.5 3.5 0 0 0 4 0zm0 5a1.4 1.4 0 1 1 0-2.8A1.4 1.4 0 0 1 4 5z"/></svg>
        218 K Avenue, Suite 310, Juneau, Alaska 99802</span>
    </footer>
  </section>

  <section class="sheet envelope-back">
    <svg class="envelope-flap" viewBox="0 0 528 90" aria-hidden="true">
      <path d="M0 0 C10 20 18 38 28 44 Q34 48 48 50 L250 83 Q264 86 278 83 L480 50 Q494 48 500 44 C510 38 518 20 528 0 Z"
            fill="var(--navy)" stroke="var(--gold)" stroke-width="1.6"/>
      <circle cx="264" cy="63" r="5" fill="var(--gold)"/>
    </svg>
  </section>
</body>
</html>
```